Business Card Design for Vantor Gear

We want to have a business card design for our company.
Company website: www.vantorgear-example.com.au
We looking for something cool, funky, and impressive, yet elegant.
Below are the contents that should be displayed on the card:
Front:
Name: Mark Dellow
Title: Sales & Purchasing
Company Name: Vantor Gear Pty Ltd
Phone: 02 5550 1473
Mobile: 0400 555 019
Email: mark@vantorgear-example.com.au
Website: www.vantorgear-example.com.au
Address: 17 Brackley St
Marlowe Park, NSW 2150
Back:
We buy sell new used Norvex and network equipment
• Huge Savings - save up to 95% off list prices
• Highest Reliability
• Comprehensive Warranty
• Fast delivery
• Large range of hardware in stock
Our logo can be downloaded at: www.vantorgear-example.com.au/logo.zip

```html
<!DOCTYPE html>
<html lang="en">
<head>
<meta charset="utf-8">
<title>Vantor Gear – Business Card</title>
<link rel="stylesheet" href="https://fonts.googleapis.com/css2?family=Comfortaa:wght@400;600;700&display=swap">
<style>
  :root {
    --stage: #6e4b34;
    --card-white: #ffffff;
    --card-blue: #00a3d5;
    --ink: #111111;
    --brand-blue: #1c6fc2;
    --label-blue: #0a8fd0;
    --mark-orange: #f07a2a;
    --line-white: #ffffff;
  }
  * { margin: 0; padding: 0; box-sizing: border-box; }
  html, body {
    width: 1200px; height: 899px; overflow: hidden;
    background: var(--stage);
    font-family: "Comfortaa", sans-serif;
  }
  .stage { position: relative; width: 1200px; height: 899px; }

  /* Front card */
  .card-front {
    position: absolute; left: 144px; top: 133px;
    width: 589px; height: 360px;
    background: var(--card-white);
    border-radius: 0 32px 0 32px;
    z-index: 2;
    color: var(--ink);
  }
  .brand { position: absolute; left: 41px; top: 32px; display: flex; align-items: center; gap: 22px; }
  .brand-dot { width: 80px; height: 80px; border-radius: 50%; background: var(--mark-orange); }
  .brand-name { font-size: 38px; font-weight: 700; color: var(--brand-blue); letter-spacing: -0.5px; }
  .person { position: absolute; left: 144px; top: 148px; }
  .person-name { font-size: 22px; font-weight: 700; letter-spacing: 1px; }
  .person-title { font-size: 16px; letter-spacing: 1.6px; margin-top: 4px; }
  .contact { position: absolute; left: 144px; top: 232px; font-size: 13.5px; line-height: 20px; }
  .contact-row { display: flex; }
  .contact-row .col-a { width: 141px; }
  .contact-address { margin-bottom: 6px; }
  .label { color: var(--label-blue); font-size: 15px; }
  .website { position: absolute; left: 144px; top: 307px; font-size: 16.5px; font-weight: 700; letter-spacing: 0.4px; }

  /* Back card */
  .card-back {
    position: absolute; left: 493px; top: 459px;
    width: 590px; height: 360px;
    background: var(--card-blue);
    border-radius: 0 0 24px 0;
    z-index: 1;
    color: var(--line-white);
  }
  .card-back svg.stitch { position: absolute; inset: 0; }
  .tagline {
    position: absolute; left: 76px; top: 72px;
    width: 438px; height: 31px;
    border: 3px solid var(--line-white); border-radius: 10px;
    font-size: 13px; font-weight: 700; letter-spacing: 0.8px;
    display: flex; align-items: center; justify-content: center;
  }
  .benefits {
    position: absolute; left: 78px; top: 125px;
    width: 376px; height: 185px;
    border: 3px solid var(--line-white); border-radius: 12px;
    list-style: none;
  }
  .benefits::before {
    content: ""; position: absolute; left: 19px; top: 18px; width: 2px; height: 142px;
    background: var(--line-white);
  }
  .benefits li {
    position: absolute; left: 10px; display: flex; align-items: center; gap: 10px;
    font-size: 12.5px; font-weight: 700; letter-spacing: 0.3px;
  }
  .benefits li::before {
    content: ""; width: 20px; height: 20px; border-radius: 50%;
    border: 2.5px solid var(--line-white);
    background: radial-gradient(circle, var(--line-white) 0 4px, var(--card-blue) 4.5px);
    box-sizing: border-box;
  }
  .benefits li:nth-child(1) { top: 7px; }
  .benefits li:nth-child(2) { top: 43px; }
  .benefits li:nth-child(3) { top: 78px; }
  .benefits li:nth-child(4) { top: 115px; }
  .benefits li:nth-child(5) { top: 150px; }
  .pointer { position: absolute; left: 520px; top: 302px; }
</style>
</head>
<body>
<main class="stage">
  <section class="card-front" aria-label="Front of business card">
    <div class="brand">
      <span class="brand-dot"></span>
      <span class="brand-name">Vantor Gear</span>
    </div>
    <div class="person">
      <p class="person-name">Mark Dellow</p>
      <p class="person-title">Sales &amp; Purchasing</p>
    </div>
    <div class="contact">
      <p class="contact-address">17 Brackley St.Marlowe Park, NSW 2150</p>
      <p class="contact-row"><span class="col-a"><span class="label">p</span> :&nbsp; 02 5550 1473</span><span><span class="label">f</span>: +62 21 555 0188</span></p>
      <p class="contact-row"><span class="col-a"><span class="label">m</span>:&nbsp; 0400 555 019</span><span><span class="label">e</span>:&nbsp; mark@vantorgear-example.com.au</span></p>
    </div>
    <p class="website">www.vantorgear-example.com.au</p>
  </section>

  <section class="card-back" aria-label="Back of business card">
    <svg class="stitch" width="590" height="360" viewBox="0 0 590 360">
      <path d="M8 9 H582 V328 Q582 351 559 351 H8 Z" fill="none" stroke="#fff" stroke-width="2" stroke-dasharray="9 7"/>
    </svg>
    <p class="tagline">We buy sell new used Norvex and network equipment</p>
    <ul class="benefits">
      <li>Huge Savings - save up to 95% off list prices</li>
      <li>Highest Reliability</li>
      <li>Comprehensive Warranty</li>
      <li>Fast delivery</li>
      <li>Large range of hardware in stock</li>
    </ul>
    <svg class="pointer" width="40" height="40" viewBox="0 0 40 40" aria-hidden="true">
      <path d="M3 3 L26 12 L18 16 L35 33 L31 37 L14 20 L10 28 Z" fill="#fff"/>
    </svg>
  </section>
</main>
</body>
</html>
```